Our private family owned investment company owns a vineyard in Napa. We want to design a label to put on our wine bottles once wine is ready. We would like artists to develop a creative design for a new label using this wording: Vineyard 48217. The dimensions of the label will be the standard label size on a 750 ml wine bottle. We appreciate creative flair, a classy look, preferably color but open to black and white too; maybe submit both ways. **As more explanation for designers, our family founded and owned a business for over 50 years and our logo was a teal colored snowflake (see attached jpeg logo). Our first plant address was numbered 48217. After our business was sold, our new family office is on located at 48217 Holloway. We have created a new business logo (see attached blue TRV logo) So the 48217 and 2 logos all have lineage and sentimental value to our family. Thank you for providing your unique creativity to this project.

Target Market(s)

to inspire conversation and reminiscing among friends and business associates when entertaining them.

Industry/Entity Type

Investment

Colors

Designer to choose colors to be used in the design.

Requirements
Must have
• Must Incorporate the wording: Vineyard 48217 - as part of the entire design and please see the attached logos (sketch of Vineyard 48217, blue snowflake logo, and TRV logo) and use any of these as a base, or part of, your new design. ** See project description for more detail on the meaning behind these logos.**

```html
<!DOCTYPE html>
<html lang="en">
<head>
<meta charset="utf-8">
<title>Vineyard 48217 – Pinot Noir Label</title>
<link rel="stylesheet" href="https://fonts.googleapis.com/css2?family=Cinzel:wght@400;600&family=Cormorant+Garamond:ital,wght@1,500&display=swap">
<style>
  :root {
    --backdrop: #d9d9d9;
    --paper: #f7f7f5;
    --ink: #141414;
    --band: #1c1c1c;
    --band-text: #ecebe8;
  }
  * { margin: 0; padding: 0; box-sizing: border-box; }
  html, body {
    width: 1200px;
    height: 800px;
    overflow: hidden;
  }
  body {
    background: var(--backdrop);
    position: relative;
  }
  .label {
    position: absolute;
    left: 240px;
    top: 60px;
    width: 720px;
    height: 680px;
    background: var(--paper);
    overflow: hidden;
  }
  .label__band {
    position: absolute;
    inset: 0;
    width: 100%;
    height: 100%;
  }
  .label__band polygon { fill: var(--band); }
  .wordmark {
    position: absolute;
    top: 70px;
    left: 0;
    width: 100%;
    text-align: center;
    font-family: "Cinzel", serif;
    font-weight: 600;
    color: var(--ink);
    line-height: 1;
  }
  .wordmark__title {
    display: block;
    font-size: 62px;
    letter-spacing: 2px;
  }
  .wordmark__number {
    display: block;
    margin-top: 10px;
    font-size: 58px;
    letter-spacing: 6px;
  }
  .house-name {
    position: absolute;
    top: 262px;
    left: 0;
    width: 100%;
    text-align: center;
    font-family: "Cinzel", serif;
    font-weight: 600;
    font-size: 74px;
    letter-spacing: 8px;
    color: var(--ink);
  }
  .varietal {
    position: absolute;
    top: 468px;
    left: 0;
    width: 100%;
    text-align: center;
    font-family: "Cinzel", serif;
    font-weight: 400;
    font-size: 52px;
    letter-spacing: 2px;
    color: var(--band-text);
  }
  .origin {
    position: absolute;
    top: 548px;
    left: 0;
    width: 100%;
    text-align: center;
    font-family: "Cormorant Garamond", serif;
    font-style: italic;
    font-weight: 500;
    font-size: 40px;
    color: var(--band-text);
  }
</style>
</head>
<body>
  <section class="label">
    <svg class="label__band" viewBox="0 0 720 680" preserveAspectRatio="none" aria-hidden="true">
      <polygon points="0,330 360,420 720,330 720,680 0,680"/>
    </svg>
    <h1 class="wordmark">
      <span class="wordmark__title">VINEYARD</span>
      <span class="wordmark__number">48217</span>
    </h1>
    <p class="house-name">TRV</p>
    <p class="varietal">PINOT NOIR</p>
    <p class="origin">Napa California</p>
  </section>
</body>
</html>
```